Veltrisk inc. Aviation website

we are looking for a very modern and luxury web design, we are an aviation based company and specialize in aircraft exports and setup of air services world wide.
we want the website to be unique, creative, luxurious, professional, and to make an statement.
we have attached the logo.
our business cards theme is black background with gold stamping, if that is the rout you want to take.
**The format we are looking for is Wordpress.**
**the website is www.veltriskinc-example.com**
** 3 pages:
1. home page: -overview/about us
-industry leading
- worldwide presence
- aerial support
2. products and services: -business aircrafts
-commercial aircrafts
-amphibious aircrafts
-operation setup
-maintenance & crew training
3. contact us
**our location: Marlow Fenwick Harbour Airfield, Hangar 6**
we do appreciate suggestions
Thank you all.
Target Market(s)
Aviation professionals, Aircraft import/export, airlines, air taxi operations
Industry/Entity Type
It Company
Number of Pages Required
3 page
Requirements
Must have
- must have a very modern and luxurious design, and must be aviation oriented, and must have the logo, must be professional looking and be animated.
Nice to have
- black, gold, and burgandy colour
Should not have
- should not be playful and cartoony.

```html
<!DOCTYPE html>
<html lang="en">
<head>
<meta charset="utf-8">
<title>Veltrisk inc. – Home</title>
<link href="https://fonts.googleapis.com/css2?family=PT+Sans:wght@400;700&family=PT+Sans+Narrow:wght@700&family=Play:wght@400&display=swap" rel="stylesheet">
<style>
  :root{
    --ink:#1f1f1f;
    --band:#000;
    --paper:#fff;
    --page:#f1f1f1;
    --rule:#d9d9d9;
    --nav-active-bg:#ececec;
    --accent:#2fb4ee;
    --burgundy:#b3121f;
    --gold:#c9a227;
    --footer:#2d2d2d;
    --footer-text:#c9c9c9;
  }
  *{box-sizing:border-box;margin:0;padding:0}
  html,body{width:1200px;height:1200px;overflow:hidden}
  body{background:var(--band);font-family:"PT Sans",sans-serif;color:var(--ink);position:relative}

  .site-header{position:absolute;top:61px;left:0;width:1200px;height:175px;background:var(--paper);
    display:flex;align-items:center;justify-content:center;gap:12px;border-bottom:2px solid var(--rule)}
  .brand-dot{width:18px;height:18px;border-radius:50%;background:var(--gold)}
  .brand-name{font-family:"PT Sans",sans-serif;font-weight:400;font-size:36px;letter-spacing:3px;color:var(--burgundy)}

  .main-nav{position:absolute;top:236px;left:0;width:1200px;height:67px;background:var(--paper);
    border-bottom:2px solid var(--rule)}
  .main-nav ul{list-style:none;display:flex;justify-content:center;height:100%;margin-left:28px}
  .main-nav li{display:flex;align-items:center;padding:0 6px;font-size:13px}
  .main-nav li.is-active{background:var(--nav-active-bg);padding:0 11px}
  .main-nav li.is-active a{color:var(--accent)}
  .main-nav a{color:var(--ink);text-decoration:none}
  .main-nav .sep{color:#999;font-size:9px;margin-left:7px}

  .hero{position:absolute;top:304px;left:0;width:1200px;height:337px;border-top:2px solid #cfcfcf;
    background:
      linear-gradient(90deg,rgba(0,0,0,0) 0%,rgba(0,0,0,0) 86%,rgba(110,100,190,.55) 90%,rgba(120,110,190,.75) 100%),
      radial-gradient(ellipse 40% 22% at 40% 62%,rgba(255,255,255,.95),rgba(255,255,255,0) 100%),
      linear-gradient(180deg,#6f6ad0 0%,#8f88db 14%,#d7d2ea 24%,#f4f1f6 40%,#ece6ef 58%,#b9aec8 72%,#d9cfd9 84%,#c8bccb 100%)}
  .hero-title{position:absolute;top:94px;left:-16px;width:100%;text-align:center;font-family:"PT Sans Narrow",sans-serif;
    font-weight:700;font-size:64px;color:#2a2a2a;letter-spacing:0.5px}
  .hero-pointer{position:absolute;top:641px;left:579px}

  .content{position:absolute;top:641px;left:0;width:1200px;height:461px;background:var(--page)}
  .tagline{position:absolute;top:35px;left:126px;width:930px;text-align:center;font-size:20px;color:#1a1a1a}
  .divider{position:absolute;top:97px;left:112px;width:952px;height:1px;background:#e0e0e0}
  .features{position:absolute;top:163px;left:0;width:100%}
  .feature{position:absolute;width:206px;height:206px}
  .feature .photo{width:206px;height:206px;border-radius:50%;box-shadow:0 0 3px rgba(0,0,0,.25)}
  .feature .label{position:absolute;left:50%;transform:translateX(-50%);background:var(--accent);
    color:#fff;font-family:"Play",sans-serif;font-size:14px;letter-spacing:.6px;height:32px;line-height:32px;padding:0 5px;white-space:nowrap}
  .f1{left:240px}
  .f1 .photo{background:
      radial-gradient(ellipse 45% 30% at 50% 88%,rgba(255,255,255,.9),rgba(255,255,255,0)),
      linear-gradient(180deg,#b9b9bb 0%,#e9e9ea 22%,#8a8c94 48%,#5d6172 62%,#c9cbd0 80%,#eeeeee 100%)}
  .f2{left:494px}
  .f2 .photo{background:
      radial-gradient(ellipse 50% 25% at 55% 48%,rgba(230,232,236,.9),rgba(230,232,236,0)),
      linear-gradient(180deg,#6c7078 0%,#b7a98f 14%,#8b9299 32%,#6f7a6a 55%,#8c97a3 75%,#3f4a58 100%)}
  .f3{left:746px}
  .f3 .photo{background:
      radial-gradient(ellipse 40% 22% at 72% 8%,rgba(210,220,228,1),rgba(210,220,228,0)),
      linear-gradient(90deg,#d2261f 0%,#b22a22 28%,#3b3f45 45%,#2b3037 70%,#55606a 100%)}
  .f1 .label{top:142px}.f2 .label{top:142px}.f3 .label{top:138px;padding:0 14px}

  .site-footer{position:absolute;top:1102px;left:0;width:1200px;height:40px;background:var(--footer);
    display:flex;align-items:center;justify-content:space-between;padding:0 112px 0 99px;font-size:10.5px;color:var(--footer-text)}
  .site-footer nav{display:flex;gap:12px;text-transform:uppercase}
  .site-footer a{color:var(--footer-text);text-decoration:none}
</style>
</head>
<body>
  <header class="site-header">
    <span class="brand-dot"></span>
    <span class="brand-name">VELTRISK</span>
  </header>

  <nav class="main-nav">
    <ul>
      <li class="is-active"><a href="#">Home</a><span class="sep">»</span></li>
      <li><a href="#">Products and Services</a><span class="sep">»</span></li>
      <li><a href="#">Contact</a><span class="sep">»</span></li>
    </ul>
  </nav>

  <section class="hero" role="img" aria-label="Business jet parked in a bright hangar with tall windows, a presenter gesturing toward it">
    <h1 class="hero-title">INDUSTRY LEADING</h1>
  </section>
  <svg class="hero-pointer" width="16" height="9" viewBox="0 0 16 9"><path d="M0 0H16L8 9Z" fill="#c8bccb"/></svg>

  <main class="content">
    <p class="tagline">VELTRISK delivers results. Our goal is to provide both a superior customer experience and tremendous value.</p>
    <div class="divider"></div>
    <div class="features">
      <div class="feature f1">
        <div class="photo" role="img" aria-label="Modern airport terminal interior with arched roof"></div>
        <span class="label">Industry Leading</span>
      </div>
      <div class="feature f2">
        <div class="photo" role="img" aria-label="Aerial view of a large airport complex"></div>
        <span class="label">Worldwide Presence</span>
      </div>
      <div class="feature f3">
        <div class="photo" role="img" aria-label="Air traffic controller working at radar screens"></div>
        <span class="label">Aerial Support</span>
      </div>
    </div>
  </main>

  <footer class="site-footer">
    <nav><a href="#">Home</a><a href="#">Products and Services</a><a href="#">Contact</a></nav>
    <span>Veltrisk | All Rights Reserved</span>
  </footer>
</body>
</html>
```